Consulting firm needs elegant, modern designs

Business card design - I have a logo which has previously been developed for K-Pathways - I will attach. I will also attach specifications for the size of the business card.

We also need a logo design for our leadership consulting product - Frame of Guidance - we focus on improving workplace health by educating leaders and learning professionals about how the physical and emotional affects performance and engagement. I have some example logos and ideas which I will attach - these have attempted to bring in the body but I do not like the font (see www.frameofguidance.example for preferred font). Idea is to please have a 'body' visible somehow in the word Leadership, ensuring that this conveys flexibility and agility. Colors which I prefer are deep purple OR turquoise, together with silver. COLORS below are for LOGO design.

Target Market(s)

For the business card, it should be more masculine. The logo which will be attached should be neutralized into dark blue shades and silver. The business card K-Pathways is focused on business transformation - organizations who would require a consultant to help them enter new markets, for example.

Industry/Entity Type

Leadership

Contact Information for Business Card

Content:
K-Pathways
Molenkade 27
4921KT, Lindenvaart, Westmarken
maarten@K-Pathways.example
www.K-Pathways.example

Colors for business card should be conservative and slightly more masculine. Use the K-Pathways logo but change the colors to blue or shades of gray/black.

Dimensions for cut
85 x 55 mm
1004 x 650 pixels
Full document size
88 x 58 mm
1040 x 685 pixels
For the best result, you need to design the full document size including the bleed

Logo Text

Frame of Guidance

Font styles to use
Serif
Sans Serif

Colors
876aae
333333
959595

Requirements
Must have
• Professional, modern and unique business card design
• Professional, elegant, and modern logo design - with creative thinking
Should not have
• Too many colors

```html
<!DOCTYPE html>
<html lang="en">
<head>
<meta charset="utf-8">
<title>K-Pathways Business Card</title>
<link rel="stylesheet" href="https://fonts.googleapis.com/css2?family=Montserrat:wght@300;500&family=Oswald:wght@500&family=Lato:wght@400&display=swap">
<style>
  :root {
    --stage: #d4d4d6;
    --navy: #221e42;
    --white: #ffffff;
    --purple: #7d5fb5;
    --teal: #3fa8a0;
    --ink: #3a3a3a;
    --grey: #5a5a5a;
    --soft: #c9c6dc;
  }
  * { box-sizing: border-box; margin: 0; padding: 0; }
  html, body { width: 1200px; height: 800px; overflow: hidden; }
  body { background: var(--stage); position: relative; font-family: "Lato", sans-serif; }

  .card {
    position: absolute;
    top: 232px;
    width: 520px;
    height: 336px;
    box-shadow: 0 6px 18px rgba(0,0,0,0.18);
  }
  .card--front { left: 50px; background: var(--navy); color: var(--white); }
  .card--back { left: 630px; background: var(--white); }

  /* Front */
  .brand {
    position: absolute;
    left: 78px;
    top: 112px;
    display: flex;
    align-items: center;
    gap: 18px;
  }
  .brand__dot {
    width: 64px; height: 64px;
    border-radius: 50%;
    background: var(--teal);
    flex: none;
  }
  .brand__name {
    font-family: "Montserrat", sans-serif;
    font-weight: 500;
    font-size: 46px;
    letter-spacing: 0.5px;
    line-height: 1;
    color: var(--white);
    white-space: nowrap;
  }
  .brand__tagline {
    font-family: "Montserrat", sans-serif;
    font-weight: 300;
    font-size: 17px;
    color: var(--soft);
    margin-top: 6px;
    white-space: nowrap;
  }
  .front__url {
    position: absolute;
    left: 0; right: 0;
    bottom: 58px;
    text-align: center;
    font-family: "Montserrat", sans-serif;
    font-weight: 500;
    font-size: 15px;
    letter-spacing: 0.6px;
    color: var(--white);
  }

  /* Back */
  .identity {
    position: absolute;
    left: 64px;
    top: 108px;
    display: flex;
    align-items: center;
  }
  .person { text-align: right; padding-right: 20px; }
  .person__name {
    font-family: "Oswald", sans-serif;
    font-weight: 500;
    font-size: 30px;
    letter-spacing: 0.5px;
    color: var(--purple);
    text-transform: uppercase;
    line-height: 1.05;
    white-space: nowrap;
  }
  .person__role {
    font-size: 14px;
    letter-spacing: 1px;
    color: var(--ink);
    text-transform: uppercase;
  }
  .divider { width: 1.5px; height: 62px; background: var(--purple); flex: none; }
  .contacts { list-style: none; padding-left: 20px; }
  .contacts li {
    display: flex;
    align-items: center;
    gap: 9px;
    font-size: 12.5px;
    color: var(--ink);
    line-height: 1.7;
    white-space: nowrap;
  }
  .contacts svg { width: 11px; height: 11px; fill: var(--purple); flex: none; }
  .address {
    position: absolute;
    left: 0; right: 0;
    bottom: 54px;
    text-align: center;
    font-size: 13.5px;
    color: var(--grey);
    letter-spacing: 0.3px;
  }
</style>
</head>
<body>

<section class="card card--front">
  <div class="brand">
    <span class="brand__dot"></span>
    <div>
      <div class="brand__name">K-Pathways</div>
      <div class="brand__tagline">Steady through each move</div>
    </div>
  </div>
  <p class="front__url">www.K-Pathways.example</p>
</section>

<section class="card card--back">
  <div class="identity">
    <div class="person">
      <div class="person__name">Daniel Verhoef</div>
      <div class="person__role">Founder</div>
    </div>
    <span class="divider"></span>
    <ul class="contacts">
      <li>
        <svg viewBox="0 0 24 24" aria-hidden="true"><path d="M6.6 10.8a15.1 15.1 0 0 0 6.6 6.6l2.2-2.2a1 1 0 0 1 1-.25 11.4 11.4 0 0 0 3.6.57 1 1 0 0 1 1 1V20a1 1 0 0 1-1 1A17 17 0 0 1 3 4a1 1 0 0 1 1-1h3.5a1 1 0 0 1 1 1c0 1.25.2 2.45.57 3.57a1 1 0 0 1-.25 1z"/></svg>
        (555) 018-2240
      </li>
      <li>
        <svg viewBox="0 0 24 24" aria-hidden="true"><path d="M2 5h20v14H2z M2 5l10 8 10-8" fill="none" stroke="#7d5fb5" stroke-width="2.4"/></svg>
        maarten@K-Pathways.example
      </li>
      <li>
        <svg viewBox="0 0 24 24" aria-hidden="true"><circle cx="12" cy="12" r="9.5" fill="none" stroke="#7d5fb5" stroke-width="2.2"/><path d="M2.5 12h19M12 2.5c3 3 3 16 0 19M12 2.5c-3 3-3 16 0 19" fill="none" stroke="#7d5fb5" stroke-width="1.8"/></svg>
        www.K-Pathways.example
      </li>
    </ul>
  </div>
  <p class="address">Molenkade 27 4921KT, Lindenvaart, Westmarken</p>
</section>

</body>
</html>
```